Brightvantage.com tech company website

Current site is www.brightvantage.com. The site will tell you about our company.

Designs we like are:
http://megainfo.quellorix.com
www.trelvo.com
www.morvasket.com

Target Market(s)

B2B

Industry/Entity Type

It Company

Coding

Coded - Design and coding required

Number of Pages Required

5+ page

Requirements
Must have
• We want to entice without giving away too much info. We like graphics and colors. But website must look official and credible.

```html
<!DOCTYPE html>
<html lang="en">
<head>
<meta charset="utf-8">
<title>Brightvantage</title>
<link href="https://fonts.googleapis.com/css2?family=Open+Sans:wght@400;600;700&family=Raleway:wght@500;600;700&display=swap" rel="stylesheet">
<style>
:root{
  --blue:#1b5c9c;
  --blue-dark:#154a80;
  --ink:#2a2f36;
  --muted:#6c737b;
  --light:#eef0f2;
  --topbar:#f3f4f5;
  --night:#0d1822;
  --footer:#101a23;
  --white:#ffffff;
}
*{box-sizing:border-box;margin:0;padding:0}
html,body{width:668px;height:1200px;overflow:hidden}
body{font-family:"Open Sans",Arial,sans-serif;color:var(--ink);background:var(--white);font-size:7px;line-height:1.5}
h1,h2,h3{font-family:"Raleway",Arial,sans-serif}
.btn{display:inline-block;background:var(--blue);color:var(--white);font-size:6.5px;font-weight:700;letter-spacing:.4px;padding:6px 14px;text-transform:uppercase}
.btn-dark{background:#2b3138}

.topbar{height:22px;background:var(--topbar);display:flex;align-items:center;padding:0 18px;font-size:6.5px;color:var(--muted);border-bottom:1px solid #e2e4e6}
.topbar .addr{flex:1;display:flex;align-items:center;gap:4px}
.topbar .contact{display:flex;gap:22px}
.topbar .contact span{display:flex;align-items:center;gap:4px;line-height:1.2}
.ico{width:9px;height:9px;flex:none}

.masthead{height:52px;display:flex;align-items:stretch;padding-left:18px;background:var(--white)}
.brand{display:flex;align-items:center;gap:6px;flex:1}
.brand .mark{width:14px;height:14px;border-radius:50%;background:var(--blue)}
.brand .name{font-family:"Raleway",sans-serif;font-weight:700;font-size:17px;color:var(--blue);letter-spacing:.3px}
.nav{display:flex;margin-right:18px}
.nav a{display:flex;align-items:center;padding:0 9px;font-size:6px;font-weight:600;color:var(--ink);text-decoration:none;text-transform:uppercase;border-left:1px solid #e6e8ea}
.nav a.active{background:var(--blue);color:var(--white)}

.hero{position:relative;height:326px;background:linear-gradient(160deg,#2d3a46 0%,#1b2731 45%,#0f1820 100%);color:var(--white);text-align:center;overflow:hidden}
.hero .photo{position:absolute;inset:0;background:radial-gradient(ellipse at 62% 40%,rgba(130,150,170,.35),transparent 60%)}
.hero .inner{position:relative;padding-top:122px}
.hero h1{font-size:36px;font-weight:500;letter-spacing:1.5px}
.hero p{width:440px;margin:10px auto 16px;font-size:7px;line-height:1.55}
.hero .dots{position:absolute;bottom:12px;right:22px;display:flex;gap:4px}
.hero .dots i{width:10px;height:3px;background:rgba(255,255,255,.4)}
.hero .dots i:first-child{background:var(--white)}

.welcome{height:166px;background:var(--light);text-align:center;padding-top:56px}
.welcome h2{font-size:17px;font-weight:600;color:var(--ink)}
.welcome h2 em{font-style:normal;color:var(--blue)}
.welcome p{width:560px;margin:8px auto 12px;color:var(--muted);font-size:6.5px}

.services{height:256px;padding:16px 26px 0}
.section-title{text-align:center;font-size:16px;font-weight:600;display:flex;justify-content:center;align-items:center;gap:6px}
.section-title .gear{width:14px;height:14px}
.cards{display:flex;gap:22px;margin-top:14px}
.card{flex:1}
.card .img{height:112px}
.card h3{font-family:"Open Sans",sans-serif;font-size:6.5px;font-weight:700;color:var(--blue);margin:8px 0 3px;text-transform:uppercase}
.card p{font-size:6px;color:var(--muted);margin-bottom:7px}

.partial{height:211px;background:var(--night);color:var(--white);padding:24px 33px 0}
.partial h2{text-align:center;font-size:15px;font-weight:600}
.partial .row{display:flex;gap:34px;margin-top:20px}
.partial .img{width:266px;height:110px;background:linear-gradient(120deg,#dfe5ea,#9aa9b6 60%,#5c6f80)}
.partial ul{list-style:none;font-size:6px;line-height:1.3}
.partial li{display:flex;align-items:center;gap:5px;margin-bottom:3.6px}

.footer{height:133px;background:var(--footer);color:#b9c1c8;display:flex;padding:26px 33px 0;gap:20px}
.footer .col{flex:1}
.footer h4{font-family:"Raleway",sans-serif;font-size:7px;font-weight:600;color:var(--white);letter-spacing:.5px;margin-bottom:10px;text-transform:uppercase}
.footer p{font-size:6px;display:flex;gap:5px;align-items:flex-start}
.footer .field{height:14px;background:var(--white);margin-bottom:4px}
.footer .signup{display:block;text-align:center;padding:4px 0}
.footer .social{display:flex;gap:6px}
.footer .social i{width:16px;height:16px;border-radius:50%;background:var(--white)}
.copyright{height:34px;background:var(--blue);color:var(--white);display:flex;align-items:center;justify-content:center;font-size:6.5px}
</style>
</head>
<body>
<header class="topbar">
  <div class="addr"><svg class="ico" viewBox="0 0 10 10"><path d="M5 1a3 3 0 0 0-3 3c0 2.2 3 5 3 5s3-2.8 3-5a3 3 0 0 0-3-3z" fill="#1b5c9c"/><circle cx="5" cy="4" r="1" fill="#fff"/></svg>Address Line1, Address line2 - 123456, Country</div>
  <div class="contact">
    <span><svg class="ico" viewBox="0 0 10 10"><rect x="1" y="2.5" width="8" height="5" fill="none" stroke="#1b5c9c"/><path d="M1 2.5l4 3 4-3" fill="none" stroke="#1b5c9c"/></svg>EMAIL US<br>info@brightvantage.com</span>
    <span><svg class="ico" viewBox="0 0 10 10"><path d="M2 1.5l2 0 .8 2-1.2.8a5 5 0 0 0 2 2l.8-1.2 2 .8v2c-4 0-7-3-6.4-6.4z" fill="#1b5c9c"/></svg>CALL US<br>+91 555 010 4821</span>
  </div>
</header>

<nav class="masthead">
  <div class="brand"><span class="mark"></span><span class="name">Brightvantage</span></div>
  <div class="nav">
    <a class="active" href="#">Home</a><a href="#">About</a><a href="#">Big Data Analytics</a><a href="#">Perception and Influence</a><a href="#">Case Studies</a><a href="#">Contact</a>
  </div>
</nav>

<section class="hero">
  <div class="photo" role="img" aria-label="Dark photo of a business professional with a network of connected data points"></div>
  <div class="inner">
    <h1>BRIGHTVANTAGE</h1>
    <p>We turn scattered business data into clear decisions. Our analysts and engineers build reporting, forecasting and insight platforms that help growing companies act sooner, spend smarter and measure every result with confidence.</p>
    <span class="btn">Read More</span>
  </div>
  <div class="dots"><i></i><i></i></div>
</section>

<section class="welcome">
  <h2>Welcome to <em>Brightvantage</em></h2>
  <p>Brightvantage partners with enterprise teams to collect, clean and connect their data. From strategy workshops to managed analytics, we deliver dependable insight that leadership can trust and teams can use every day without extra effort or delay.</p>
  <span class="btn">Read More</span>
</section>

<section class="services">
  <h2 class="section-title"><svg class="gear" viewBox="0 0 14 14"><circle cx="7" cy="7" r="4.5" fill="none" stroke="#1b5c9c" stroke-width="2.4" stroke-dasharray="2.2 1.3"/><circle cx="7" cy="7" r="1.6" fill="#1b5c9c"/></svg>Our Service</h2>
  <div class="cards">
    <div class="card">
      <div class="img" role="img" aria-label="Photo of a business team gathered around a laptop" style="background:linear-gradient(135deg,#e9ecef,#b7c0c8 55%,#6e7a86)"></div>
      <h3>Precision Audience Marketing</h3>
      <p>Reach the right buyers with segments built from verified behaviour and intent signals.</p>
      <span class="btn btn-dark">Read More</span>
    </div>
    <div class="card">
      <div class="img" role="img" aria-label="Photo of a dial gauge labelled leads" style="background:linear-gradient(135deg,#f1f1f1,#c9c9c9 50%,#8a4a3a)"></div>
      <h3>Lead Generation</h3>
      <p>Fill your pipeline with qualified prospects ready to talk with your sales team.</p>
      <span class="btn btn-dark">Read More</span>
    </div>
    <div class="card">
      <div class="img" role="img" aria-label="Photo of hands using a smartphone and laptop" style="background:linear-gradient(135deg,#cfe0ee,#6f98bd 55%,#2e5a82)"></div>
      <h3>Data Enhancement</h3>
      <p>Enrich existing records with accurate firmographic details and fresh contact data.</p>
      <span class="btn btn-dark">Read More</span>
    </div>
  </div>
</section>

<section class="partial">
  <h2>What can we do? Here's a partial list</h2>
  <div class="row">
    <div class="img" role="img" aria-label="Photo of a hand drawing a rising growth chart"></div>
    <ul>
      <li><svg class="ico" viewBox="0 0 10 10"><path d="M3 2l3 3-3 3" fill="none" stroke="#fff"/></svg>Make people feel positively about you and your company.</li>
      <li><svg class="ico" viewBox="0 0 10 10"><path d="M3 2l3 3-3 3" fill="none" stroke="#fff"/></svg>Change the conversation away from issues you want removed.</li>
      <li><svg class="ico" viewBox="0 0 10 10"><path d="M3 2l3 3-3 3" fill="none" stroke="#fff"/></svg>Create buzz, trends, and demand for products and services.</li>
      <li><svg class="ico" viewBox="0 0 10 10"><path d="M3 2l3 3-3 3" fill="none" stroke="#fff"/></svg>Move business owners to complete projects in the face of opposition.</li>
      <li><svg class="ico" viewBox="0 0 10 10"><path d="M3 2l3 3-3 3" fill="none" stroke="#fff"/></svg>Repair tarnished reputations.</li>
      <li><svg class="ico" viewBox="0 0 10 10"><path d="M3 2l3 3-3 3" fill="none" stroke="#fff"/></svg>Make deals happen.</li>
      <li><svg class="ico" viewBox="0 0 10 10"><path d="M3 2l3 3-3 3" fill="none" stroke="#fff"/></svg>Generate traffic to a website or physical location.</li>
    </ul>
  </div>
</section>

<footer class="footer">
  <div class="col">
    <h4>Location</h4>
    <p><svg class="ico" viewBox="0 0 10 10"><path d="M5 1a3 3 0 0 0-3 3c0 2.2 3 5 3 5s3-2.8 3-5a3 3 0 0 0-3-3z" fill="#1b5c9c"/></svg><span>14 Harbor Crest Lane<br>Suite 402<br>Linwood, 46001</span></p>
  </div>
  <div class="col">
    <h4>Stay Informed</h4>
    <div class="field"></div>
    <span class="btn signup">Sign Up</span>
  </div>
  <div class="col">
    <h4>Contact Us</h4>
    <p><svg class="ico" viewBox="0 0 10 10"><path d="M2 1.5l2 0 .8 2-1.2.8a5 5 0 0 0 2 2l.8-1.2 2 .8v2c-4 0-7-3-6.4-6.4z" fill="#1b5c9c"/></svg>+1 555 014 2290</p>
    <p><svg class="ico" viewBox="0 0 10 10"><path d="M2 1.5l2 0 .8 2-1.2.8a5 5 0 0 0 2 2l.8-1.2 2 .8v2c-4 0-7-3-6.4-6.4z" fill="#1b5c9c"/></svg>+1 555 014 2291</p>
    <p><svg class="ico" viewBox="0 0 10 10"><rect x="1" y="2.5" width="8" height="5" fill="none" stroke="#1b5c9c"/><path d="M1 2.5l4 3 4-3" fill="none" stroke="#1b5c9c"/></svg>contact@brightvantage.com</p>
  </div>
  <div class="col">
    <h4>Follow Us</h4>
    <div class="social"><i></i><i></i><i></i><i></i></div>
  </div>
</footer>
<div class="copyright">© Copyright 2015. All Rights Reserved</div>
</body>
</html>
```